Ongoing work and Exhibition stand design for Harbin Panels

I need a simple layout/sketch for a 3 x 3m stand for a trade show (see examples of stand designs below). It is a corner stand so will only have 2 walls for display. There will be a TV on one wall. One island bench or table will be needed to write on and display flyers.

The stand is a shell scheme which means it has a floor, lights and an aluminium frame already supplied.

We sell kitchen doors (and wardrobe doors). I need to show sample doors 300 x 400mm but can make them in any size to suit. I want a simple but original way of showing the doors and I want the stand to be noticed!

Headline graphics to include the text "Renovating your kitchen? Just replace the doors, saving you thousands of $$$. Improve the value of your home at a fraction of the cost." Graphics to include kitchen picture(s) attached.

The main colour scheme would be the orange of our brochure (see brochure attached).

Ongoing work will probably be offered to the winner of this project.

Needed ASAP! Thanks.

Target Market(s)

The do it yourself DIY home renovator. Male and female home owners age group 25-55.

Industry/Entity Type

Trade

Requirements
Must have
• Clean and simple but eye catching design.

```html
<!DOCTYPE html>
<html lang="en">
<head>
<meta charset="utf-8">
<title>Harbin Panels – Exhibition Stand Wall Graphics</title>
<link rel="stylesheet" href="https://fonts.googleapis.com/css2?family=Anton&family=Archivo+Black&family=Arimo:wght@700&family=Libre+Baskerville:ital,wght@0,700;1,700&display=swap">
<style>
  :root {
    --orange: #f39a1d;
    --orange-deep: #e07a10;
    --orange-light: #fbc36a;
    --navy: #12305a;
    --blue: #1f5fb0;
    --ink: #1d1d1d;
    --white: #ffffff;
    --door-teal: #2f6f86;
    --door-slate: #5f8298;
    --door-green: #35a27f;
    --door-sky: #9cc9ef;
    --backdrop: #161616;
  }
  * { margin: 0; padding: 0; box-sizing: border-box; }
  html, body { width: 1200px; height: 867px; overflow: hidden; background: var(--backdrop); }
  .stand-graphics {
    position: relative; width: 1200px; height: 867px; overflow: hidden;
    background: linear-gradient(180deg, var(--orange-light) 0%, var(--orange) 60%, var(--orange-deep) 100%);
  }
  .wall { position: absolute; top: 0; bottom: 0; }
  .wall-left { left: 0; width: 780px; }
  .wall-right { left: 780px; width: 420px; border-left: 3px solid rgba(0,0,0,0.25); }

  .header-band {
    position: absolute; left: 0; top: 0; width: 1200px; height: 230px;
    background: linear-gradient(180deg, var(--orange-deep) 0%, var(--orange) 55%, var(--orange-light) 100%);
  }
  .kitchen-photo {
    position: absolute; top: 230px; height: 380px;
    background: linear-gradient(180deg, rgba(255,244,220,0.95) 0%, rgba(245,215,160,0.85) 60%, rgba(243,154,29,0) 100%);
  }
  .kitchen-photo.left { left: 0; width: 780px; }
  .kitchen-photo.right { left: 3px; width: 417px; }

  .headline-left {
    position: absolute; left: 110px; top: 130px; display: flex; align-items: flex-end; gap: 10px;
  }
  .is-your {
    font-family: "Archivo Black", sans-serif; color: var(--blue); line-height: 0.9;
    display: flex; flex-direction: column; align-items: center;
  }
  .is-your .is { font-size: 52px; letter-spacing: 2px; }
  .is-your .your { font-size: 23px; }
  .kitchen-word {
    font-family: "Archivo Black", sans-serif; font-size: 84px; line-height: 0.9; color: var(--white);
    text-shadow: 3px 3px 0 var(--ink);
  }
  .brand {
    position: absolute; left: 640px; top: 140px; display: flex; align-items: center; gap: 8px;
    font-family: "Arimo", sans-serif; font-weight: 700; font-size: 19px; line-height: 1.05; color: var(--navy);
  }
  .brand .mark { width: 18px; height: 18px; background: var(--white); flex: none; }

  .headline-right {
    position: absolute; left: 800px; top: 130px; display: flex; align-items: flex-end; gap: 8px;
  }
  .need-of {
    font-family: "Arimo", sans-serif; font-weight: 700; color: var(--ink);
    font-size: 16px; line-height: 1.05; text-align: right; padding-bottom: 6px;
  }
  .makeover {
    font-family: "Anton", sans-serif; font-size: 60px; line-height: 1; color: var(--white);
    text-shadow: 3px 3px 0 var(--ink);
  }

  .renovating {
    position: absolute; left: 370px; top: 250px;
    font-family: "Libre Baskerville", serif; font-style: italic; font-weight: 700;
    font-size: 44px; color: var(--ink); letter-spacing: 1px;
  }
  .improve {
    position: absolute; left: 250px; top: 305px;
    font-family: "Arimo", sans-serif; font-weight: 700; font-size: 34px; color: var(--ink);
  }
  .your-kitchen {
    position: absolute; left: 800px; top: 258px;
    font-family: "Libre Baskerville", serif; font-weight: 700; font-size: 30px; color: var(--ink);
  }
  .fraction {
    position: absolute; left: 805px; top: 307px;
    font-family: "Arimo", sans-serif; font-weight: 700; font-size: 22px; color: var(--ink);
  }

  .delivery-ribbon { position: absolute; right: 0; top: 230px; width: 150px; height: 150px; }

  .door { position: absolute; border: 2px solid rgba(0,0,0,0.2); }
  .door-teal { left: 300px; top: 385px; width: 170px; height: 190px; background: var(--door-teal); }
  .door-slate { left: 495px; top: 385px; width: 160px; height: 190px; background: var(--door-slate); }
  .door-green { left: 850px; top: 390px; width: 120px; height: 230px; background: var(--door-green); }
  .door-sky { left: 990px; top: 390px; width: 120px; height: 230px; background: var(--door-sky); }

  .quality-badge { position: absolute; left: 668px; top: 362px; width: 95px; height: 95px; }

  .contact-line {
    position: absolute; left: 560px; top: 630px; width: 630px;
    font-family: "Arimo", sans-serif; font-weight: 700; font-size: 11px; color: var(--ink); line-height: 1.6;
  }
  .floor-band {
    position: absolute; left: 0; bottom: 0; width: 1200px; height: 150px;
    background: linear-gradient(180deg, var(--orange) 0%, var(--orange-deep) 100%);
    border-top: 2px solid rgba(0,0,0,0.15);
  }
</style>
</head>
<body>
<main class="stand-graphics">
  <div class="header-band"></div>

  <section class="wall wall-left">
    <div class="kitchen-photo left" role="img" aria-label="Faded photograph of a bright renovated kitchen with white cabinets and stone benchtop"></div>
  </section>
  <section class="wall wall-right">
    <div class="kitchen-photo right" role="img" aria-label="Faded photograph of a kitchen and living area with lamp"></div>
  </section>

  <div class="headline-left">
    <div class="is-your"><span class="is">IS</span><span class="your">YOUR</span></div>
    <div class="kitchen-word">KITCHEN</div>
  </div>

  <div class="brand"><span class="mark"></span><span>Harbin<br>Panels</span></div>

  <div class="headline-right">
    <div class="need-of">NEED<br>OF A</div>
    <div class="makeover">MAKEOVER?</div>
  </div>

  <p class="renovating">RENOVATING</p>
  <p class="improve">Improve the value of your</p>
  <p class="your-kitchen">YOUR KITCHEN</p>
  <p class="fraction">home at a fraction of the cost</p>

  <svg class="delivery-ribbon" viewBox="0 0 150 150" aria-label="Australia wide delivery">
    <polygon points="20,0 150,0 150,130" fill="var(--navy)"/>
    <g transform="translate(112 38) rotate(45)" fill="var(--white)" font-family="Arimo, sans-serif" font-weight="700" font-size="11" text-anchor="middle">
      <text x="0" y="-6">AUSTRALIA</text>
      <text x="0" y="9">WIDE</text>
      <text x="0" y="24">DELIVERY</text>
    </g>
  </svg>

  <div class="door door-teal" role="img" aria-label="Sample kitchen door in teal"></div>
  <div class="door door-slate" role="img" aria-label="Sample kitchen door in slate blue"></div>
  <div class="door door-green" role="img" aria-label="Sample wardrobe door in green"></div>
  <div class="door door-sky" role="img" aria-label="Sample wardrobe door in light blue"></div>

  <svg class="quality-badge" viewBox="0 0 100 100" aria-hidden="true">
    <circle cx="50" cy="50" r="48" fill="var(--white)"/>
    <circle cx="50" cy="50" r="40" fill="var(--navy)"/>
  </svg>

  <div class="floor-band"></div>

  <div class="contact-line">
    <p>Quality Kitchen Doors &amp; Service</p>
    <p>18 Larch Road, Millbrook NSW 2164 Ph 02 5550 1234 Fax 02 5550 5678 Email sales@harbinpanels.com.au</p>
  </div>
</main>
</body>
</html>
```